Food broker, trader, wholesaler, liquidator looking for a 5 pages website

Looking for a 5 pages website design. We are food brokers, traders, wholesaler and closeout buyer working with manufacturers, distributors, importers sell to retailers, food service operators and industrial (ingredients). We help market their products. We are a resource for those who need a solution in the distribution/selling/placement of food on the shelves, kitchens and pantries. Whether we open new accounts with new products or sell short dated inventory, we know where to go and get results.

Target Market(s)

Food manufacturers, food distributors, food brokers

Coding

Coded - Design and coding required

Number of Pages Required

4 page

Font styles to use
Serif

Requirements
Must have
• Food-food production-warehouse-Food packaging-people meeting-trucks-supermarket shelves-

```html
<!DOCTYPE html>
<html lang="en">
<head>
<meta charset="utf-8">
<title>Harborline Provisions</title>
<link href="https://fonts.googleapis.com/css2?family=Montserrat:wght@400;500;600;700;800&family=Raleway:wght@300;400;500;600&family=Yanone+Kaffeesatz:wght@300;400&display=swap" rel="stylesheet">
<style>
:root{
  --navy:#10146a;
  --navy-deep:#0a0d3d;
  --footer:#06082c;
  --blue:#1429f0;
  --ink:#1d1d1d;
  --grey-bg:#ececec;
  --white:#ffffff;
  --muted:#6d6d6d;
}
*{margin:0;padding:0;box-sizing:border-box}
html,body{width:1200px;height:3932px;overflow:hidden}
body{position:relative;font-family:'Montserrat',sans-serif;color:var(--ink);background:var(--white)}
.abs{position:absolute}
.center{left:0;width:1200px;text-align:center}

/* hero */
.hero{left:0;top:0;width:1200px;height:600px;background:linear-gradient(180deg,#2a2f3c 0%,#4a4650 35%,#5b4b48 60%,#6e6f78 85%,#8d8f96 100%)}
.hero-shade{left:0;top:0;width:1200px;height:600px;background:linear-gradient(90deg,rgba(120,20,20,.25),rgba(20,60,120,.2),rgba(140,40,30,.25))}
.topbar{left:0;top:0;width:1200px;height:34px;border-bottom:1px solid rgba(255,255,255,.35);color:#fff;font-size:11px}
.topbar .call{left:113px;top:9px;display:flex;align-items:center;gap:6px}
.topbar .mail{right:120px;top:9px;display:flex;align-items:center;gap:6px}
.brand{left:113px;top:44px;display:flex;align-items:center;gap:10px;color:#fff;font-family:'Raleway',sans-serif;font-weight:600;font-size:11px;letter-spacing:.5px;text-transform:uppercase}
.brand .dot{width:76px;height:54px;border-radius:50%;background:var(--navy)}
.nav{left:594px;top:66px;display:flex;gap:29px;color:#fff;font-family:'Raleway',sans-serif;font-size:14px;letter-spacing:1.5px}
.nav a{color:#fff;text-decoration:none;padding-bottom:6px}
.nav a.active{border-bottom:4px solid #fff}
.hero-title{top:212px;font-family:'Yanone Kaffeesatz',sans-serif;font-weight:300;font-size:50px;color:#fff}
.hero-sub{top:271px;font-family:'Raleway',sans-serif;font-size:17px;color:#fff;letter-spacing:.3px}
.btn{display:inline-block;height:40px;border-radius:20px;font-size:13px;letter-spacing:2.5px;line-height:40px;text-align:center}
.btn-read{left:433px;top:322px;width:148px;background:var(--blue);color:#fff}
.btn-quote{left:593px;top:322px;width:162px;background:#fff;color:var(--ink)}
.dots{left:552px;top:386px;display:flex;gap:4px}
.dots span{width:11px;height:11px;border-radius:50%;background:#fff}
.dots span.off{background:transparent;border:1.5px solid #fff}

/* intro */
.intro-wash{left:0;top:600px;width:1200px;height:180px;background:linear-gradient(180deg,#f2f2f2,#fff)}
.intro-title{top:676px;font-family:'Montserrat',sans-serif;font-weight:500;font-size:25px;color:var(--navy)}
.intro-text{top:740px;left:240px;width:720px;text-align:center;font-size:14.5px;line-height:23px}
.more-link{top:874px;font-size:10px;letter-spacing:2.5px;color:var(--navy)}
.more-link span{border-bottom:1px solid var(--navy);padding-bottom:2px}

.warehouse{left:0;top:961px;width:1200px;height:584px;background:linear-gradient(135deg,#c7623a 0%,#d9c9a6 25%,#8f8a7c 45%,#3c57a6 60%,#caa57a 75%,#6d8d3a 100%)}

/* what we do */
.section-title{font-family:'Montserrat',sans-serif;font-weight:500;font-size:24px;color:var(--navy);letter-spacing:.5px}
.wwd-title{top:1652px}
.service{top:1713px;width:300px;height:267px;background:var(--navy);color:#fff;text-align:center;box-shadow:0 4px 10px rgba(0,0,0,.15)}
.service svg{margin-top:48px}
.service h3{font-size:14px;font-weight:700;margin-top:26px;letter-spacing:.3px}
.service p{font-size:14px;line-height:20px;color:#c9cbe6;margin:2px auto 0;width:210px}
.pride{top:2060px;font-size:18px;line-height:28.5px}
.welcome{top:2200px;font-size:23px;color:var(--navy)}

/* featured products */
.fp-title{top:2350px}
.product{top:2412px;width:238px;height:363px;overflow:hidden;background:var(--navy);color:#fff;text-align:center}
.product .photo{position:absolute;left:0;top:0;width:238px;height:200px;clip-path:polygon(0 0,100% 0,100% 58%,0 100%)}
.product .ico{position:absolute;left:89px;top:135px;width:64px;height:64px;border-radius:50%;background:#fff;display:flex;align-items:center;justify-content:center}
.product h3{position:absolute;left:0;width:238px;top:210px;font-weight:800;font-size:26px;line-height:26px}
.product p{position:absolute;left:28px;width:182px;font-size:12.5px;line-height:18px}
.product .frost{position:absolute;left:0;bottom:0;width:238px;height:40px;background:linear-gradient(180deg,rgba(255,255,255,0),rgba(255,255,255,.9))}

/* testimonials */
.people{left:0;top:2855px;width:1200px;height:393px;background:var(--grey-bg)}
.people-title{top:2900px;font-family:'Raleway',sans-serif;font-size:36px;color:#333}
.avatar{border-radius:50%;background:linear-gradient(160deg,#d8d8d8,#8d8d8d);border:2px solid #fff}
.quote{top:3068px;left:320px;width:560px;text-align:center;font-style:italic;font-size:14px;line-height:22.5px}
.author{top:3186px;left:554px;width:94px;text-align:center;font-style:italic;font-size:13px;letter-spacing:1.5px;color:#444;border-bottom:1px solid #333;padding-bottom:4px}

/* contact */
.footer{left:0;top:3455px;width:1200px;height:477px;background:var(--footer)}
.contact-frame{left:243px;top:3248px;width:715px;height:260px;background:var(--footer)}
.contact-box{left:266px;top:3272px;width:668px;height:236px;background:#fff}
.contact-box h2{position:absolute;left:0;width:668px;top:34px;text-align:center;font-family:'Raleway',sans-serif;font-weight:500;font-size:19px;letter-spacing:-.5px}
.field{position:absolute;border:1px solid #999;font-size:9px;letter-spacing:1px;padding:11px 10px;color:#333}
.submit{position:absolute;left:332px;top:154px;width:281px;height:36px;background:var(--blue);color:#fff;font-size:11px;text-align:center;line-height:36px}

.f-brand{left:113px;top:3580px;width:128px;height:90px;border-radius:50%;background:var(--navy)}
.f-name{left:113px;top:3676px;color:#fff;font-family:'Raleway',sans-serif;font-weight:600;font-size:11px;letter-spacing:.5px;text-transform:uppercase}
.f-about{left:113px;top:3698px;width:200px;color:#fff;font-size:12px;line-height:17px}
.f-col h4{font-size:13px;font-weight:500;letter-spacing:1px;color:#fff;margin-bottom:16px}
.f-col a{display:block;color:#fff;font-size:12px;text-decoration:none;margin-bottom:16px}
.f-line{display:flex;gap:14px;color:#fff;font-size:11.5px;line-height:18px;margin-bottom:18px}
.news-input{width:248px;height:36px;background:#fff;color:#888;font-size:13px;padding:9px 16px}
.news-btn{width:248px;height:36px;background:var(--blue);color:#fff;font-size:13px;text-align:center;line-height:36px;margin-top:8px}
.socials{display:flex;gap:6px;margin-top:18px}
.socials span{width:40px;height:40px;border-radius:50%}
.copyright{top:3821px;font-size:13px;font-weight:600;color:#fff}
.copyright b{color:#3b54ff}
</style>
</head>
<body>

<div class="abs hero" role="img" aria-label="Supermarket aisle with stocked shelves"></div>
<div class="abs hero-shade"></div>
<svg class="abs" style="left:0;top:520px" width="1200" height="80" viewBox="0 0 1200 80" aria-hidden="true">
  <path d="M0 40 L60 55 L120 30 L180 50 L240 28 L300 48 L360 32 L420 52 L480 26 L540 46 L600 34 L660 56 L720 30 L780 48 L840 24 L900 44 L960 28 L1020 46 L1080 20 L1140 38 L1200 22 L1200 80 L0 80 Z" fill="#f2f2f2"/>
</svg>

<div class="abs topbar">
  <div class="abs call">
    <svg width="12" height="12" viewBox="0 0 24 24"><path d="M6 2l4 4-2 3c1 3 4 6 7 7l3-2 4 4-3 4C10 21 3 14 2 5z" fill="none" stroke="#fff" stroke-width="2"/></svg>
    Call Us : 040-5521-6608
  </div>
  <div class="abs mail">
    <svg width="16" height="12" viewBox="0 0 24 18"><path d="M1 8L23 1 17 17 11 11z" fill="#fff"/></svg>
    Email : hello@harborline.example
  </div>
</div>

<div class="abs brand"><span class="dot"></span>Harborline Provisions</div>
<nav class="abs nav">
  <a class="active">Home</a><a>About US</a><a>What we do</a><a>Contact</a><a>Giving Back</a>
</nav>

<div class="abs center hero-title">Harborline Provisions works with food manufacturers,</div>
<div class="abs center hero-sub">brand owners, distributors and wholesalers market their products.</div>
<div class="abs btn btn-read">Read More</div>
<div class="abs btn btn-quote">Free quote</div>
<div class="abs dots"><span class="off"></span><span></span><span></span><span></span></div>

<div class="abs intro-wash"></div>
<div class="abs center intro-title">Retail, Food Service and Industrial ingredients.</div>
<p class="abs intro-text">Retail, Food Service and Industrial ingredients.<br>Founded in 2008, Harborline Provisions started with the distribution of gluten free products understanding the need to provide access to unique flavors and products for the celiac consumers. From this, we expanded into deli, dairy, groceries, frozen and beverages.</p>
<div class="abs center more-link"><span>READ MORE</span></div>

<div class="abs warehouse" role="img" aria-label="Warehouse store with pallets of packaged food and produce"></div>

<h2 class="abs center section-title wwd-title">WHAT WE DO</h2>

<div class="abs service" style="left:113px">
  <svg width="52" height="54" viewBox="0 0 52 54" fill="none" stroke="#fff" stroke-width="2.5"><rect x="4" y="6" width="44" height="30"/><path d="M26 36v16M18 52h16M26 12l3 6 6 1-5 4 1 6-5-3-5 3 1-6-5-4 6-1z"/></svg>
  <h3>Sales &amp; Marketing:</h3>
  <p>we connect food buyers and sellers through a dedicated approach.</p>
</div>
<div class="abs service" style="left:450px">
  <svg width="56" height="54" viewBox="0 0 56 54" fill="none" stroke="#fff" stroke-width="2.5"><path d="M20 4v20M14 18l6 6 6-6M34 24V4M28 10l6-6 6 6M4 40h14l10 4h14l10-6M18 50h20"/></svg>
  <h3>Trading</h3>
  <p>we connect food buyers and sellers through a dedicated approach.</p>
</div>
<div class="abs service" style="left:786px;top:1711px">
  <svg width="52" height="54" viewBox="0 0 52 54" fill="none" stroke="#fff" stroke-width="2.5"><path d="M4 20L26 4 48 20V50H4z"/><rect x="14" y="30" width="10" height="20"/><rect x="28" y="30" width="10" height="20"/><rect x="21" y="18" width="10" height="10"/></svg>
  <h3>Closeout/Excess Inventory</h3>
  <p>we connect food buyers and sellers through a dedicated approach.</p>
</div>

<p class="abs center pride">We pride ourselves in working in an easy, personal and accessible<br>environment making our customers and vendors comfortable with us.<br>We look forward to connecting with you and evaluating how we can assist<br>you reaching your sales objectives.</p>
<p class="abs center welcome">Welcome and thank you for visiting harborlineprovisions.com</p>

<h2 class="abs center section-title fp-title">FEATURED PRODUCTS</h2>

<div class="abs product" style="left:113px">
  <div class="photo" role="img" aria-label="Deli sandwich on a board" style="background:linear-gradient(160deg,#3a2a22,#a9642f,#5b3a26)"></div>
  <div class="ico"><svg width="34" height="34" viewBox="0 0 34 34" fill="none" stroke="var(--navy)" stroke-width="2"><circle cx="17" cy="17" r="13"/><path d="M8 24L26 10M12 14l8 8"/></svg></div>
  <h3>DELI</h3>
  <p style="top:256px">Founded in 2008, Harborline Provisions started with the distribution.</p>
  <div class="frost"></div>
</div>
<div class="abs product" style="left:357px">
  <div class="photo" role="img" aria-label="Nuts and grains in bowls with jars" style="background:linear-gradient(160deg,#8a7a6a,#c9b39a,#6b4a36)"></div>
  <div class="ico"><svg width="34" height="34" viewBox="0 0 34 34" fill="none" stroke="var(--navy)" stroke-width="2"><path d="M12 4h10v6l4 6v14H8V16l4-6z"/><path d="M8 20h18"/></svg></div>
  <h3>DAIRY</h3>
  <p style="top:256px">Founded in 2008, Harborline Provisions started with the distribution.</p>
  <div class="frost"></div>
</div>
<div class="abs product" style="left:602px">
  <div class="photo" role="img" aria-label="Basket of fresh groceries and vegetables" style="background:linear-gradient(160deg,#f4f4f4,#5fae3a,#e2b93a,#2aa68b)"></div>
  <div class="ico"><svg width="34" height="34" viewBox="0 0 34 34" fill="var(--navy)"><rect x="4" y="14" width="12" height="16"/><rect x="18" y="10" width="12" height="20"/><rect x="6" y="6" width="3" height="8"/><rect x="11" y="4" width="3" height="10"/></svg></div>
  <h3>GROCERIES</h3>
  <p style="top:256px">Founded in 2008, Harborline Provisions started with the distribution.</p>
  <div class="frost"></div>
</div>
<div class="abs product" style="left:846px">
  <div class="photo" role="img" aria-label="Colourful cocktails in glasses" style="background:linear-gradient(160deg,#121212,#d6452d,#f08a3a,#1a1a1a)"></div>
  <div class="ico"><svg width="34" height="34" viewBox="0 0 34 34" fill="none" stroke="var(--navy)" stroke-width="2"><path d="M8 10h18l-3 20H11zM20 10l4-7M9 18h16"/></svg></div>
  <h3>FROZEN AND<br>BEVERAGES</h3>
  <p style="top:278px">Founded in 2008, Harborline Provisions started with the distribution.</p>
  <div class="frost"></div>
</div>

<div class="abs people"></div>
<div class="abs center people-title">People Say</div>
<svg class="abs" style="left:456px;top:2992px" width="16" height="22" viewBox="0 0 16 22"><path d="M12 3L4 11l8 8" fill="none" stroke="#888" stroke-width="3"/></svg>
<svg class="abs" style="left:733px;top:2992px" width="16" height="22" viewBox="0 0 16 22"><path d="M4 3l8 8-8 8" fill="none" stroke="#888" stroke-width="3"/></svg>
<div class="abs avatar" style="left:487px;top:2980px;width:46px;height:46px" role="img" aria-label="Customer portrait"></div>
<div class="abs avatar" style="left:560px;top:2960px;width:82px;height:82px;border-width:4px" role="img" aria-label="Customer portrait"></div>
<div class="abs avatar" style="left:670px;top:2980px;width:46px;height:46px" role="img" aria-label="Customer portrait"></div>
<p class="abs quote">Lorem Ipsum is simply dummy text of the printing and typesetting industry. Lorem Ipsum has been the industry's standard dummy text ever since the 1500s, when an unknown printer took a galley of type and scrambled it to make a type specimen book.</p>
<div class="abs author">Dana Whitfield</div>

<div class="abs footer"></div>
<div class="abs contact-frame"></div>
<div class="abs contact-box">
  <h2>GET IN IN TOUCH</h2>
  <div class="field" style="left:47px;top:70px;width:281px;height:36px">NAME:</div>
  <div class="field" style="left:47px;top:112px;width:281px;height:36px">EMAIL:</div>
  <div class="field" style="left:47px;top:154px;width:281px;height:36px">PHONE:</div>
  <div class="field" style="left:332px;top:70px;width:281px;height:78px;padding-top:8px">COMMENTS :</div>
  <div class="submit">SUBMIT NOW</div>
</div>

<div class="abs f-brand"></div>
<div class="abs f-name">Harborline Provisions</div>
<p class="abs f-about">Lorem Ipsum is simply dummy text of the printing and typesetting industry.</p>

<div class="abs f-col" style="left:389px;top:3578px">
  <h4>SITEMAP</h4>
  <a>Home</a><a>About US</a><a>What we do</a><a>Contact</a><a>Giving Back</a>
</div>

<div class="abs f-col" style="left:567px;top:3578px">
  <h4>GET IN TOUCH</h4>
  <div class="f-line"><svg width="14" height="18" viewBox="0 0 14 18"><path d="M7 1a6 6 0 0 1 6 6c0 5-6 10-6 10S1 12 1 7a6 6 0 0 1 6-6z" fill="var(--blue)"/><circle cx="7" cy="7" r="2" fill="var(--footer)"/></svg><span>118 Quayside Road, 3rd Floor<br>Bayford, CA 90210 USA</span></div>
  <div class="f-line"><svg width="14" height="14" viewBox="0 0 24 24"><path d="M6 2l4 4-2 3c1 3 4 6 7 7l3-2 4 4-3 4C10 21 3 14 2 5z" fill="none" stroke="var(--blue)" stroke-width="2"/></svg><span>(+100) 555 204 19</span></div>
  <div class="f-line"><svg width="16" height="12" viewBox="0 0 24 18"><path d="M1 8L23 1 17 17 11 11z" fill="var(--blue)"/></svg><span>info@harborline.example</span></div>
</div>

<div class="abs f-col" style="left:838px;top:3578px">
  <h4>NEWSLETTER SUBSCRIBE</h4>
  <div class="news-input">Enter your email id :</div>
  <div class="news-btn">NEWSLETTER SUBSCRIBE</div>
  <div class="socials">
    <span style="background:#3b5ba8"></span><span style="background:#1da1f2"></span><span style="background:#0a78b5"></span><span style="background:#e1261c"></span>
  </div>
</div>

<div class="abs center copyright">Copyright © 2020 <b>Harborline Provisions</b></div>

</body>
</html>
```